RTB CONTRACTING

I am looking for a logo/design for my business. Would like some unique symbol, would also like it to be double sided. On the back perhaps 3 pictures of some work we have done. I will attach some photos.

I would also like the colours to be orange and black or a dark grey and Orange.

Only writing I would like to see are:

(Contact number) 416-382-7164
(Name) Derek Holloway
(Email) dholloway@mailbox-example.ca

```html
<!DOCTYPE html>
<html lang="en">
<head>
<meta charset="utf-8">
<title>RTB Contracting – Business Card</title>
<link href="https://fonts.googleapis.com/css2?family=Cinzel:wght@500;600&family=Roboto:wght@400;700&display=swap" rel="stylesheet">
<style>
  :root {
    --page-bg: #d9d9d9;
    --panel-grey: #4a4a4a;
    --brand-orange: #e0692a;
    --text-white: #ffffff;
    --text-soft: #e6e6e6;
    --card-shadow: rgba(0, 0, 0, 0.28);
  }
  html, body {
    margin: 0;
    padding: 0;
    width: 1200px;
    height: 864px;
    overflow: hidden;
    background: var(--page-bg);
  }
  .canvas {
    position: relative;
    width: 1200px;
    height: 864px;
  }
  .card {
    position: absolute;
    width: 540px;
    height: 309px;
    overflow: hidden;
    box-shadow: 0 10px 28px var(--card-shadow);
    background: #fff;
  }
  /* Front side */
  .card--front { left: 50px; top: 420px; }
  .front-panel {
    position: absolute;
    left: 0; top: 0;
    width: 300px; height: 100%;
    background: var(--panel-grey);
    color: var(--text-white);
  }
  .brand {
    position: absolute;
    left: 36px; top: 40px;
    display: flex;
    align-items: center;
    gap: 12px;
  }
  .brand-square {
    width: 34px; height: 34px;
    background: var(--brand-orange);
  }
  .brand-name {
    font-family: "Cinzel", serif;
    font-weight: 600;
    font-size: 19px;
    letter-spacing: 0.5px;
    color: var(--brand-orange);
    white-space: nowrap;
  }
  .person {
    position: absolute;
    left: 36px; top: 118px;
  }
  .person-name {
    font-family: "Roboto", sans-serif;
    font-weight: 700;
    font-size: 20px;
    letter-spacing: 1px;
    text-transform: uppercase;
    margin: 0;
  }
  .person-title {
    font-family: "Roboto", sans-serif;
    font-size: 13px;
    color: var(--text-soft);
    margin: 4px 0 0;
  }
  .contact {
    position: absolute;
    left: 36px; top: 210px;
    list-style: none;
    margin: 0; padding: 0;
    font-family: "Roboto", sans-serif;
    font-size: 13px;
    color: var(--text-white);
  }
  .contact li {
    display: flex;
    align-items: center;
    gap: 10px;
    margin-bottom: 8px;
    white-space: nowrap;
  }
  .contact svg { width: 14px; height: 14px; flex: none; }
  .front-photo {
    position: absolute;
    left: 300px; top: 0;
    width: 240px; height: 100%;
    background: linear-gradient(150deg, #f2f2f2 0%, #e8e6df 35%, #d8b56c 60%, #e6d23a 78%, #2b2b2b 100%);
  }
  /* Back side */
  .card--back { left: 610px; top: 130px; }
  .back-photo {
    position: absolute;
    inset: 0;
    background: linear-gradient(160deg, #e9ecee 0%, #b9a48a 35%, #9a6a3e 65%, #6b4424 100%);
  }
  .back-brand {
    position: absolute;
    right: 34px; bottom: 40px;
    font-family: "Cinzel", serif;
    font-weight: 600;
    font-size: 30px;
    color: var(--brand-orange);
    white-space: nowrap;
  }
</style>
</head>
<body>
<main class="canvas">
  <section class="card card--back" aria-label="Card back">
    <div class="back-photo" role="img" aria-label="Photo of a finished open-plan kitchen and living room renovation"></div>
    <div class="back-brand">RTB Contracting</div>
  </section>

  <section class="card card--front" aria-label="Card front">
    <div class="front-panel">
      <div class="brand">
        <span class="brand-square"></span>
        <span class="brand-name">RTB Contracting</span>
      </div>
      <div class="person">
        <p class="person-name">Derek Holloway</p>
        <p class="person-title">Managing Director</p>
      </div>
      <ul class="contact">
        <li>
          <svg viewBox="0 0 24 24" aria-hidden="true"><path fill="#fff" d="M6.6 10.8a15.1 15.1 0 0 0 6.6 6.6l2.2-2.2c.3-.3.7-.4 1-.2 1.1.4 2.3.6 3.6.6.6 0 1 .4 1 1V20c0 .6-.4 1-1 1A17 17 0 0 1 3 4c0-.6.4-1 1-1h3.5c.6 0 1 .4 1 1 0 1.3.2 2.5.6 3.6.1.3 0 .7-.2 1z"/></svg>
          416-382-7164
        </li>
        <li>
          <svg viewBox="0 0 24 24" aria-hidden="true"><rect x="2.5" y="5" width="19" height="14" fill="none" stroke="#fff" stroke-width="1.6"/><path d="M2.5 5l9.5 8 9.5-8" fill="none" stroke="#fff" stroke-width="1.6"/></svg>
          dholloway@mailbox-example.ca
        </li>
      </ul>
    </div>
    <div class="front-photo" role="img" aria-label="Photo of carpentry tools: hand saw, hammer and pine boards"></div>
  </section>
</main>
</body>
</html>
```